Offshore Energy Projects Management Consultancy needs a business card design

Logo available. We provide teams to deliver engineering consultancy, project management and delivery teams mainly in the offshore renewables sector. The company is all about bringing the right people to a project to deliver the scope.

The business card will be used for all staff.

The business card should be quite simple, vibrant and uncluttered but convey experience, enthusiasm and integration.

Target Market(s)

Energy Project Developers and Tier 1 construction companies

Contact Information for Business Card

Logo should be on the back of the card. I'm happy for the designer to play with the colour of the logo and background colour.

Front of the card should convey all the must have information in a clear and professional manner but without being overly traditional.

Colors

Designer to choose colors to be used in the design.

Requirements
Must have
• Land Line Tel Number, Mobile Tel Number, Email, business address, web address.

```html
<!DOCTYPE html>
<html lang="en">
<head>
<meta charset="utf-8">
<title>Tidewater Works Group – Business Card</title>
<link href="https://fonts.googleapis.com/css2?family=Open+Sans:wght@400;600;700&display=swap" rel="stylesheet">
<style>
  :root{
    --bg:#c9c9c9;
    --paper:#ffffff;
    --navy:#2a5aa8;
    --sky:#2e93db;
    --ink:#555a60;
    --muted:#6b7076;
  }
  *{box-sizing:border-box;margin:0;padding:0}
  html,body{width:1200px;height:852px;overflow:hidden}
  body{background:var(--bg);font-family:"Open Sans",Arial,sans-serif;position:relative}

  .card{position:absolute;width:520px;height:298px;background:var(--paper);border-radius:14px;overflow:hidden;box-shadow:0 6px 18px rgba(0,0,0,.18)}
  .card--back{left:50px;top:277px}
  .card--front{left:630px;top:277px}

  .wordmark{display:flex;align-items:center;gap:12px;font-weight:700;color:var(--navy);letter-spacing:.5px;text-transform:uppercase;white-space:nowrap}
  .wordmark__dot{width:22px;height:22px;border-radius:50%;background:var(--navy);flex:none}

  /* back */
  .card--back .wordmark{position:absolute;left:0;right:0;top:104px;justify-content:center;font-size:27px}
  .card--back .web{position:absolute;left:0;right:0;top:176px;text-align:center;font-size:14px;color:var(--ink);letter-spacing:.3px}
  .dash{position:absolute;height:2px;width:36px;background:var(--sky)}
  .dash--left{left:132px;top:186px}
  .dash--right{right:132px;top:186px}
  .band{position:absolute;left:0;right:0;bottom:0;height:12px;display:flex}
  .band__navy{flex:1;background:var(--navy)}
  .band__sky{flex:1;background:var(--sky)}
  .dash--foot{left:242px;bottom:34px}

  /* front */
  .card--front .wordmark{position:absolute;left:32px;top:124px;font-size:18px;gap:10px}
  .card--front .wordmark__dot{width:20px;height:20px}
  .person{position:absolute;right:32px;top:44px;text-align:right}
  .person__name{font-size:20px;font-weight:700;color:var(--navy)}
  .person__role{font-size:12px;color:var(--ink)}
  .rule{position:absolute;height:1px;background:var(--sky)}
  .rule--top{right:32px;top:100px;width:250px}
  .rule--bottom{left:32px;right:32px;top:184px;background:var(--navy)}
  .contacts{position:absolute;left:32px;right:32px;top:196px;list-style:none;font-size:12.5px;color:var(--ink)}
  .contacts li{display:flex;align-items:center;gap:8px;height:22px;white-space:nowrap}
  .contacts svg{width:13px;height:13px;fill:var(--navy);flex:none}
  .contacts .gap{margin-left:14px}
</style>
</head>
<body>

<section class="card card--back" aria-label="Card back">
  <div class="wordmark"><span class="wordmark__dot"></span>Tidewater Works Group</div>
  <span class="dash dash--left"></span>
  <span class="dash dash--right"></span>
  <p class="web">www.tidewaterworks.com</p>
  <span class="dash dash--foot"></span>
  <div class="band"><span class="band__navy"></span><span class="band__sky"></span></div>
</section>

<section class="card card--front" aria-label="Card front">
  <div class="person">
    <p class="person__name">Daniel Harrow</p>
    <p class="person__role">Managing Director</p>
  </div>
  <span class="rule rule--top"></span>
  <div class="wordmark"><span class="wordmark__dot"></span>Tidewater Works Group</div>
  <span class="rule rule--bottom"></span>
  <ul class="contacts">
    <li>
      <svg viewBox="0 0 16 16"><path d="M3 2h3l1 3-2 1.5a9 9 0 0 0 4.5 4.5L11 9l3 1v3a1 1 0 0 1-1 1A12 12 0 0 1 2 3a1 1 0 0 1 1-1z"/></svg>
      020 555 0142
      <svg class="gap" viewBox="0 0 16 16"><path d="M3 2h3l1 3-2 1.5a9 9 0 0 0 4.5 4.5L11 9l3 1v3a1 1 0 0 1-1 1A12 12 0 0 1 2 3a1 1 0 0 1 1-1z"/></svg>
      033 555 0198
    </li>
    <li>
      <svg viewBox="0 0 16 16"><path d="M8 1a5 5 0 0 0-5 5c0 4 5 9 5 9s5-5 5-9a5 5 0 0 0-5-5zm0 7a2 2 0 1 1 0-4 2 2 0 0 1 0 4z"/></svg>
      78 Harbour Row, Portside, Seaford, ST 40218
    </li>
    <li>
      <svg viewBox="0 0 16 16"><path d="M1 3h14v10H1z M1 3l7 6 7-6" fill="none" stroke="#2a5aa8" stroke-width="1.6"/></svg>
      daniel@tidewaterworks.com
      <svg class="gap" viewBox="0 0 16 16"><circle cx="8" cy="8" r="6.5" fill="none" stroke="#2a5aa8" stroke-width="1.4"/><path d="M1.5 8h13M8 1.5c-3 3-3 10 0 13M8 1.5c3 3 3 10 0 13" fill="none" stroke="#2a5aa8" stroke-width="1.2"/></svg>
      www.tidewaterworks.com
    </li>
  </ul>
</section>

</body>
</html>
```